Food fans website needs a desktop homepage design

We need a desktop homepage design for Zestmora.co.uk, a website to help you to find the best restaurants in each main city of Europe, with initial focus on London. It is not a directory with thousands of restaurants and reviews, else lists of top 20 restaurants for each area of the city. Food fans from all around the city will be able to keep an itinerary of where they eat, showing them later funny stats like "this month you really went for pizzas, don't you?". Keep it funny but professional.

A bit of branding has been done but this project give you total freedom to design the homepage of the site. The design must be a mix between minimal, flat and clean layout. The main idea is to keep it simple, easy to use and showing just the necessary elements.

For the font and colour scheme, we would like to use a thin but energetic font using the #E1393A colour as starting point even if you have freedom to slightly modify it. Blacks, greys and whites can be the secondary colours but we are open to introduce another main colour to the site like green, orange or yellow.

A simple wireframe has been attached to help you but the main elements that the page requires are the next:
- Panoramic fancy image in the header to contain the logo and the search form (the fields of the form are specified on the wireframe) and maybe some animated text to fill the right gap.
- List of results (10 results per page) showing the main info for each restaurant: name, thumbnail, location (zone, area), category, price, description, rating (no with stars please) and whatever you want to add that makes sense.
- Right hand sidebar with 3 widgets: Categories, Location and prices.

You can get the icons from vendrako.net.

We are open to have some text-shadows, rounded corners, box-shadows but trying to keep it minimal, flat and clean as much as possible. The main attractive of the site are the food/restaurant images.

Target Market(s)

22 - 45 food fans lovers from the city. busy people that want to disconnect and relax through the food. The don't mind to pay for quality and new experiences. Up to meet new places around them.

Industry/Entity Type

Restaurant

Requirements
Must have
• Panoramic image in the header, restaurants search form as per wireframe, list results with pagination, right hand sidebar with the widgets mention above and a nice footer with extra elements like "latest restaurants, latest tweets, etc.."
Nice to have
• This site will only be supported by the latest browsers so the idea is to have nice CSS3 transitions all around. Have that in mind at the time to design it even if you cannot show it on the design.
Should not have
• Busy backgrounds and unnecessary images that would slow down the page load.

```html
<!DOCTYPE html>
<html lang="en">
<head>
<meta charset="utf-8">
<title>Zestmora – Know where to eat in London</title>
<link href="https://fonts.googleapis.com/css2?family=Open+Sans:ital,wght@0,300;0,400;0,600;0,700;1,400&display=swap" rel="stylesheet">
<style>
:root{
  --red:#e1393a;
  --ink:#222;
  --text:#555;
  --muted:#888;
  --line:#dcdcdc;
  --panel:#efefef;
  --count:#c4c4c4;
  --white:#fff;
}
*{box-sizing:border-box;margin:0;padding:0}
html,body{width:864px;height:1200px;overflow:hidden}
body{font-family:"Open Sans",sans-serif;background:var(--white);color:var(--text);position:relative}

/* Hero */
.hero{position:absolute;left:0;top:0;width:864px;height:404px;border-top:3px solid var(--red);overflow:hidden}
.hero-photo{position:absolute;inset:0;background:
  radial-gradient(ellipse 260px 160px at 300px 250px,#6a3a22 0%,#3d2418 50%,transparent 100%),
  radial-gradient(ellipse 200px 120px at 640px 300px,#8d8a86 0%,#4a4644 60%,transparent 100%),
  linear-gradient(180deg,#1b1614 0%,#2a211d 55%,#3b3532 80%,#4a4542 100%)}
.hero-shade{position:absolute;inset:0;background:rgba(0,0,0,.35)}
.brand{position:absolute;left:116px;top:21px;display:flex;align-items:center;gap:10px}
.brand-dot{width:37px;height:37px;border-radius:50%;background:var(--red)}
.brand-name{color:var(--white);font-weight:600;font-size:15px;letter-spacing:.5px}
.tagline{position:absolute;left:116px;top:88px;color:var(--white);font-size:20px;font-weight:400;letter-spacing:.3px;padding-bottom:6px;border-bottom:1px solid rgba(255,255,255,.8);width:161px;white-space:nowrap}
.headline{position:absolute;left:116px;top:127px;color:var(--white);font-size:24px;font-weight:700;line-height:25px;text-transform:uppercase}

.search-field{position:absolute;height:22px;border-bottom:1px solid rgba(255,255,255,.45);color:#eee;font-size:13px;letter-spacing:.8px;display:flex;justify-content:space-between;align-items:flex-start}
.field-restaurant{left:122px;top:212px;width:266px}
.field-where{left:428px;top:212px;width:268px}
.field-food{left:122px;top:261px;width:266px}
.field-price{left:428px;top:261px;width:268px}
.search-field svg{margin-right:6px}
.field-price em{font-style:italic;letter-spacing:.2px}
.price-range{font-weight:600;letter-spacing:1.5px}
.slider-track{position:absolute;left:470px;top:282px;width:73px;height:2px;background:var(--red)}
.slider-knob{position:absolute;top:277px;width:11px;height:11px;border-radius:50%;background:var(--white)}
.search-btn{position:absolute;left:122px;top:306px;width:266px;height:43px;background:rgba(225,57,58,.85);border:1px solid rgba(255,255,255,.35);color:#f6d4d4;font-size:12px;letter-spacing:1.5px;display:flex;align-items:center;justify-content:center}

/* Title band */
.band{position:absolute;left:0;top:404px;width:864px;height:68px;background:var(--white);border-top:1px solid #222;border-bottom:1px solid var(--line)}
.band-title{position:absolute;left:116px;top:24px;font-size:15px;font-weight:400;color:#666;display:flex;align-items:center;gap:7px;letter-spacing:.3px}
.band-title strong{color:var(--red);font-weight:600}
.band-divider{position:absolute;left:528px;top:8px;width:1px;height:52px;background:var(--line)}
.follow{position:absolute;left:545px;top:23px;display:flex;align-items:center;gap:8px;font-size:13px;color:#aaa;font-weight:300}
.follow-link{display:flex;align-items:center;gap:3px;color:#999;font-weight:400;font-size:11px}
.follow-link i{width:9px;height:9px;border-radius:50%;background:#c8c8c8;display:block}

/* Content */
.content{position:absolute;left:0;top:472px;width:864px;height:631px;background:var(--panel)}
.results{position:absolute;left:116px;top:17px;width:412px}
.result{position:relative;height:90px;margin-bottom:5px;background:var(--white);border:1px solid #e2e2e2;border-left:4px solid var(--red)}
.result-photo{position:absolute;left:0;top:0;width:121px;height:88px}
.result-body{position:absolute;left:136px;top:7px;width:236px}
.result-name{font-size:13px;color:var(--ink);font-weight:400;letter-spacing:.3px;line-height:17px}
.result-meta{font-size:9.5px;color:var(--muted);line-height:13px}
.result-tags{font-size:9px;line-height:12px;color:var(--red);font-weight:600}
.result-tags span{color:#999;font-weight:400}
.result-desc{font-size:7.4px;line-height:9.3px;color:#666;margin-top:3px}
.result-edge{position:absolute;right:0;top:0;width:24px;height:65px;background:#f7f7f7;display:flex;flex-direction:column;align-items:center;justify-content:center}
.result-score{font-size:10px;font-weight:700;color:var(--ink);line-height:12px}
.result-score-label{font-size:6px;color:#999;letter-spacing:.3px}
.result-go{position:absolute;right:-1px;bottom:-1px;width:24px;height:24px;background:var(--red);display:flex;align-items:center;justify-content:center}

.pagination{position:absolute;left:116px;top:597px;width:412px;display:flex;gap:4px;align-items:center}
.page{width:24px;height:24px;background:var(--white);border:1px solid #e2e2e2;font-size:11px;color:#666;display:flex;align-items:center;justify-content:center}
.page.current{background:var(--red);border-color:var(--red);color:var(--white);font-weight:600}
.page-info{margin-left:auto;font-size:10px;color:#999}

.sidebar{position:absolute;left:542px;top:17px;width:208px}
.widget{margin-bottom:22px}
.widget-head{display:flex;justify-content:space-between;align-items:center;height:25px;border-bottom:2px solid #dedede;color:var(--red);font-size:12.5px;font-weight:600;letter-spacing:.3px;margin-bottom:8px}
.widget-item{display:flex;height:32px;margin-bottom:4px;background:var(--white);border:1px solid #e4e4e4}
.widget-item span{flex:1;display:flex;align-items:center;padding-left:11px;font-size:13px;font-weight:600;color:#555;letter-spacing:.3px}
.widget-item b{width:39px;background:var(--count);color:#f4f4f4;font-weight:400;font-size:12px;display:flex;align-items:center;justify-content:center}
.widget-item.tall{height:50px;margin-bottom:5px}
.widget-item.tall span{font-size:12.5px;line-height:15px}

/* Footer */
.footer{position:absolute;left:0;top:1103px;width:864px;height:97px;background:var(--white);border-top:1px solid #e0e0e0}
.footer-col{position:absolute;top:14px;width:200px}
.footer-col h5{font-size:10px;font-weight:600;color:var(--red);letter-spacing:.5px;margin-bottom:5px}
.footer-col li{list-style:none;font-size:10px;line-height:15px;color:#888}
.footer-col.latest{left:116px}
.footer-col.chirps{left:336px;width:190px}
.footer-col.about{left:542px;width:208px}
.footer-note{position:absolute;left:0;right:0;bottom:8px;text-align:center;font-size:9px;color:#bbb;font-weight:600}
</style>
</head>
<body>

<header class="hero">
  <div class="hero-photo" role="img" aria-label="Close-up photograph of a gourmet burger with a small dip bowl on a plate in a dim restaurant"></div>
  <div class="hero-shade"></div>
  <div class="brand"><span class="brand-dot"></span><span class="brand-name">Zestmora</span></div>
  <p class="tagline">Food Fans in London</p>
  <h1 class="headline">Know where to eat,<br>wherever you are.</h1>

  <div class="search-field field-restaurant">What restaurant?
    <svg width="18" height="18" viewBox="0 0 18 18" fill="none" stroke="#ddd" stroke-width="1.3"><path d="M3 15L13 5M5 17L15 7M12 2l4 4"/></svg></div>
  <div class="search-field field-where">Where?
    <svg width="12" height="16" viewBox="0 0 12 16" fill="none" stroke="#ddd" stroke-width="1.3"><path d="M6 15s5-5.5 5-9A5 5 0 0 0 1 6c0 3.5 5 9 5 9z"/><circle cx="6" cy="6" r="1.8"/></svg></div>
  <div class="search-field field-food">What kind of food?
    <svg width="18" height="16" viewBox="0 0 18 16" fill="none" stroke="#ddd" stroke-width="1.3"><path d="M2 8h14a7 6 0 0 1-14 0zM8 5l6-4M9 5l5-2"/></svg></div>
  <div class="search-field field-price"><span>Prices? <em>(slide to set range)</em></span><span class="price-range">$20 – 100</span></div>
  <div class="slider-track"></div>
  <div class="slider-knob" style="left:465px"></div>
  <div class="slider-knob" style="left:538px"></div>

  <div class="search-btn">SEARCH</div>
</header>

<section class="band">
  <h2 class="band-title">
    <svg width="15" height="13" viewBox="0 0 15 13"><path d="M7.5 13L1.2 6.6A3.6 3.6 0 0 1 7.5 2a3.6 3.6 0 0 1 6.3 4.6z" fill="var(--red)"/></svg>
    <span>BEST RESTAURANTS IN <strong>LONDON</strong></span>
  </h2>
  <div class="band-divider"></div>
  <div class="follow">FOLLOW US:
    <span class="follow-link"><i></i>Plume</span>
    <span class="follow-link"><i></i>Chirpa</span>
    <span class="follow-link"><i></i>Orbix</span>
  </div>
</section>

<main class="content">
  <div class="results">
    <article class="result">
      <div class="result-photo" role="img" aria-label="Diners at a candlelit table inside a brick-walled pub" style="background:linear-gradient(135deg,#5a3a2c,#2a1c16)"></div>
      <div class="result-body"><h3 class="result-name">The Copper Ladle</h3><p class="result-meta">12 Marlow Row, London • 5.6km from you</p><p class="result-tags">Pubs <span>• Camden • £20–£30</span></p><p class="result-desc">Lorem ipsum dolor sit amet, consectetur adipisicing elit, sed do eiusmod tempor incididunt ut labore et dolore magna aliqua. Ut enim ad minim veniam, quis nostrud...</p></div>
      <div class="result-edge"><span class="result-score">9.1</span><span class="result-score-label">/10</span></div>
      <div class="result-go"><svg width="8" height="10" viewBox="0 0 8 10" fill="none" stroke="#fff" stroke-width="1.6"><path d="M2 1l4 4-4 4"/></svg></div>
    </article>
    <article class="result">
      <div class="result-photo" role="img" aria-label="Wood-panelled restaurant interior with bar stools" style="background:linear-gradient(135deg,#6b4030,#24160f)"></div>
      <div class="result-body"><h3 class="result-name">Harbour Table</h3><p class="result-meta">12 Marlow Row, London • 5.6km from you</p><p class="result-tags">Italian <span>• Southwark • £30–£50</span></p><p class="result-desc">Lorem ipsum dolor sit amet, consectetur adipisicing elit, sed do eiusmod tempor incididunt ut labore et dolore magna aliqua. Ut enim ad minim veniam, quis nostrud...</p></div>
      <div class="result-edge"><span class="result-score">8.8</span><span class="result-score-label">/10</span></div>
      <div class="result-go"><svg width="8" height="10" viewBox="0 0 8 10" fill="none" stroke="#fff" stroke-width="1.6"><path d="M2 1l4 4-4 4"/></svg></div>
    </article>
    <article class="result">
      <div class="result-photo" role="img" aria-label="Dark shopfront of a steakhouse on a stone city building" style="background:linear-gradient(180deg,#b9b3a8,#5a5550 45%,#22201e)"></div>
      <div class="result-body"><h3 class="result-name">Brasswick Grill</h3><p class="result-meta">12 Marlow Row, London • 5.6km from you</p><p class="result-tags">Steakhouse <span>• West London • £30–£50</span></p><p class="result-desc">Lorem ipsum dolor sit amet, consectetur adipisicing elit, sed do eiusmod tempor incididunt ut labore et dolore magna aliqua. Ut enim ad minim veniam, quis nostrud...</p></div>
      <div class="result-edge"><span class="result-score">8.5</span><span class="result-score-label">/10</span></div>
      <div class="result-go"><svg width="8" height="10" viewBox="0 0 8 10" fill="none" stroke="#fff" stroke-width="1.6"><path d="M2 1l4 4-4 4"/></svg></div>
    </article>
    <article class="result">
      <div class="result-photo" role="img" aria-label="Japanese restaurant front with glowing windows at night" style="background:linear-gradient(135deg,#7a3b40,#2c1a26 60%,#3a2a30)"></div>
      <div class="result-body"><h3 class="result-name">Umiko</h3><p class="result-meta">12 Marlow Row, London • 5.6km from you</p><p class="result-tags">Japanese <span>• North London • £20–£30</span></p><p class="result-desc">Lorem ipsum dolor sit amet, consectetur adipisicing elit, sed do eiusmod tempor incididunt ut labore et dolore magna aliqua. Ut enim ad minim veniam, quis nostrud...</p></div>
      <div class="result-edge"><span class="result-score">8.2</span><span class="result-score-label">/10</span></div>
      <div class="result-go"><svg width="8" height="10" viewBox="0 0 8 10" fill="none" stroke="#fff" stroke-width="1.6"><path d="M2 1l4 4-4 4"/></svg></div>
    </article>
    <article class="result">
      <div class="result-photo" role="img" aria-label="Rooftop dining room overlooking city lights at night" style="background:linear-gradient(180deg,#0e1a3a,#1f2a55 50%,#3a2a1c)"></div>
      <div class="result-body"><h3 class="result-name">Rosewell Roast</h3><p class="result-meta">12 Marlow Row, London • 5.6km from you</p><p class="result-tags">Grill <span>• West London • £20–£30</span></p><p class="result-desc">Lorem ipsum dolor sit amet, consectetur adipisicing elit, sed do eiusmod tempor incididunt ut labore et dolore magna aliqua. Ut enim ad minim veniam, quis nostrud...</p></div>
      <div class="result-edge"><span class="result-score">7.9</span><span class="result-score-label">/10</span></div>
      <div class="result-go"><svg width="8" height="10" viewBox="0 0 8 10" fill="none" stroke="#fff" stroke-width="1.6"><path d="M2 1l4 4-4 4"/></svg></div>
    </article>
    <article class="result">
      <div class="result-photo" role="img" aria-label="Fast food restaurant building with striped awnings" style="background:linear-gradient(180deg,#e8ecef,#c9c4c0 55%,#8a7a70)"></div>
      <div class="result-body"><h3 class="result-name">Crumbwell Chicken</h3><p class="result-meta">12 Marlow Row, London • 5.6km from you</p><p class="result-tags">Fast Food <span>• Southwark • £10–£20</span></p><p class="result-desc">Lorem ipsum dolor sit amet, consectetur adipisicing elit, sed do eiusmod tempor incididunt ut labore et dolore magna aliqua. Ut enim ad minim veniam, quis nostrud...</p></div>
      <div class="result-edge"><span class="result-score">7.4</span><span class="result-score-label">/10</span></div>
      <div class="result-go"><svg width="8" height="10" viewBox="0 0 8 10" fill="none" stroke="#fff" stroke-width="1.6"><path d="M2 1l4 4-4 4"/></svg></div>
    </article>
  </div>

  <nav class="pagination" aria-label="Results pages">
    <span class="page current">1</span>
    <span class="page">2</span>
    <span class="page">3</span>
    <span class="page">4</span>
    <span class="page"><svg width="8" height="10" viewBox="0 0 8 10" fill="none" stroke="#666" stroke-width="1.6"><path d="M2 1l4 4-4 4"/></svg></span>
    <span class="page-info">Showing 1–10 of 20</span>
  </nav>

  <aside class="sidebar">
    <section class="widget">
      <h4 class="widget-head">CATEGORIES
        <svg width="17" height="14" viewBox="0 0 17 14" fill="var(--red)"><rect y="0" width="17" height="2"/><rect y="4" width="17" height="2"/><rect y="8" width="17" height="2"/><rect x="5" y="12" width="12" height="2"/></svg></h4>
      <div class="widget-item"><span>Pubs</span><b>23</b></div>
      <div class="widget-item"><span>Italian</span><b>23</b></div>
      <div class="widget-item"><span>Thai</span><b>9</b></div>
      <div class="widget-item"><span>Indian</span><b>15</b></div>
      <div class="widget-item"><span>Japanese</span><b>12</b></div>
    </section>
    <section class="widget">
      <h4 class="widget-head">LOCATIONS
        <svg width="18" height="17" viewBox="0 0 18 17" fill="var(--red)"><rect x="0" y="0" width="2" height="17"/><path d="M2 1h12l-3 4 4 4H2z"/></svg></h4>
      <div class="widget-item"><span>West London</span><b>23</b></div>
      <div class="widget-item"><span>North London</span><b>23</b></div>
      <div class="widget-item"><span>Southwark</span><b>23</b></div>
    </section>
    <section class="widget">
      <h4 class="widget-head">PRICES <span style="font-size:18px;font-weight:700">£</span></h4>
      <div class="widget-item tall"><span>Casual Restaurants<br>£10–£20</span><b>21</b></div>
      <div class="widget-item tall"><span>High Class Restaurants<br>£30–£50</span><b>21</b></div>
    </section>
  </aside>
</main>

<footer class="footer">
  <div class="footer-col latest">
    <h5>LATEST RESTAURANTS</h5>
    <ul><li>Umiko – Japanese, North London</li><li>Harbour Table – Italian, Southwark</li></ul>
  </div>
  <div class="footer-col chirps">
    <h5>LATEST ON CHIRPA</h5>
    <ul><li>New top 20 for Southwark is live!</li><li>This month you really went for pizzas…</li></ul>
  </div>
  <div class="footer-col about">
    <h5>ZESTMORA</h5>
    <ul><li>About · Contact · Cities</li><li>hello@zestmora.co.uk</li></ul>
  </div>
  <p class="footer-note">© Zestmora.co.uk – Food Fans in London</p>
</footer>

</body>
</html>
```